Apricot Variety Sheet - Meadowlark Orchard Co

We are needing a variety sheet that we can hand out that will describe the different apricot vatieties we have available. The attached document has the name of the variety along with a description that will need to be on the sheet. We are looking for a modern, appealing way to display this information on 1 page (if needed, it can be front and back)
Updates

Apologies for the delay; we are overwhelmed with the great design options and will be sorting through them all (across our contests) to pick a collective. Thank you for your patience.

Target Market(s)

Growers and consumers

Industry/Entity Type

Agriculture

Requirements
Must have
• Easy to read
• Natural color palettes to emphasize the agricultural nature
• Clearly show washington as the origin in the title or at the top
Nice to have
• incorporate Apricots in the design

```html
<!DOCTYPE html>
<html lang="en">
<head>
<meta charset="utf-8">
<title>Washington Apricot Varieties – Meadowlark Orchard Co</title>
<link href="https://fonts.googleapis.com/css2?family=Source+Sans+3:wght@400;700&display=swap" rel="stylesheet">
<style>
  :root {
    --frame-green: #006838;
    --paper: #eef5dc;
    --fruit-light: #f4f0b4;
    --fruit-deep: #eedf8e;
    --leaf: #cfe3b4;
    --heading-orange: #f15a2b;
    --body-ink: #1d1d1b;
  }
  * { box-sizing: border-box; margin: 0; padding: 0; }
  html, body {
    width: 848px;
    height: 1200px;
    overflow: hidden;
    background: var(--frame-green);
  }
  .sheet {
    position: relative;
    width: 848px;
    height: 1200px;
    background: var(--frame-green);
    padding: 27px;
  }
  .sheet-inner {
    position: relative;
    width: 794px;
    height: 1146px;
    background: var(--paper);
    overflow: hidden;
  }
  .apricot-backdrop {
    position: absolute;
    inset: 0;
    background:
      radial-gradient(ellipse 150px 160px at 170px 140px, var(--fruit-light) 0%, rgba(244,240,180,0) 100%),
      radial-gradient(ellipse 160px 150px at 560px 170px, var(--fruit-light) 0%, rgba(244,240,180,0) 100%),
      radial-gradient(ellipse 150px 170px at 120px 560px, var(--fruit-deep) 0%, rgba(238,223,142,0) 100%),
      radial-gradient(ellipse 160px 170px at 650px 560px, var(--fruit-light) 0%, rgba(244,240,180,0) 100%),
      radial-gradient(ellipse 90px 120px at 560px 680px, var(--leaf) 0%, rgba(207,227,180,0) 100%),
      radial-gradient(ellipse 150px 150px at 130px 940px, var(--fruit-deep) 0%, rgba(238,223,142,0) 100%),
      radial-gradient(ellipse 170px 160px at 500px 960px, var(--fruit-light) 0%, rgba(244,240,180,0) 100%),
      radial-gradient(ellipse 140px 150px at 730px 950px, var(--fruit-light) 0%, rgba(244,240,180,0) 100%);
    opacity: 0.85;
  }
  .sheet-header {
    position: absolute;
    left: 147px;
    top: 38px;
    width: 502px;
    text-align: center;
    font-family: "Source Sans 3", "Myriad Pro", sans-serif;
  }
  .sheet-title {
    font-weight: 700;
    font-size: 34px;
    line-height: 40px;
    color: var(--frame-green);
  }
  .sheet-grower {
    font-weight: 400;
    font-size: 16px;
    line-height: 22px;
    color: var(--body-ink);
  }
  .variety-list {
    position: absolute;
    left: 147px;
    top: 122px;
    width: 502px;
    font-family: "Source Sans 3", "Myriad Pro", sans-serif;
  }
  .variety + .variety { margin-top: 8px; }
  .variety-name {
    font-weight: 700;
    font-size: 44px;
    line-height: 44px;
    color: var(--heading-orange);
    text-align: center;
  }
  .variety-description {
    font-weight: 400;
    font-size: 16px;
    line-height: 20.5px;
    color: var(--body-ink);
    text-align: justify;
    text-align-last: center;
  }
</style>
</head>
<body>
<div class="sheet">
  <div class="sheet-inner">
    <div class="apricot-backdrop" role="img" aria-label="Faint photograph of whole and halved apricots with a green leaf"></div>
    <header class="sheet-header">
      <h1 class="sheet-title">Washington Apricot Varieties</h1>
      <p class="sheet-grower">Grown by Meadowlark Orchard Co</p>
    </header>
    <main class="variety-list">
      <section class="variety">
        <h2 class="variety-name">Tomcot</h2>
        <p class="variety-description">Tangy, sweet flavor with a firm texture. This oval apricot is light orange with a slight blush color. The flesh is a dark orange. Available late June – late July.</p>
      </section>
      <section class="variety">
        <h2 class="variety-name">Goldrich</h2>
        <p class="variety-description">This apricot is round with a bright orange skin color and a deep orange flesh. It has a mild, sweet flavor with a firm texture. Available early July – mid August.</p>
      </section>
      <section class="variety">
        <h2 class="variety-name">Casselbrite</h2>
        <p class="variety-description">This medium sized apricot is golden orange with a slight red blush. It has a mild sweet-tart flavor that is good for eating out of hand. Available late June – early July.</p>
      </section>
      <section class="variety">
        <h2 class="variety-name">Goldbar</h2>
        <p class="variety-description">Moderately juicy, this large oval-shaped apricot has a light yellow-orange with a reddish blush. The flesh is firm, meaty, and has a light orange color. Available late June – end of July.</p>
      </section>
      <section class="variety">
        <h2 class="variety-name">Sweet Juillet</h2>
        <p class="variety-description">This special variety has a unique, sweet flavor with a juicy flesh. It is bright orange in color with a bright orange flesh. Available through July.</p>
      </section>
      <section class="variety">
        <h2 class="variety-name">Tasty Rich</h2>
        <p class="variety-description">This early variety is light yellow-orange colored with a firm texture. Very juicy with an enticing flavor. Available through June.</p>
      </section>
      <section class="variety">
        <h2 class="variety-name">Goldstrike</h2>
        <p class="variety-description">A larger apricot with light orange, blushed skin. Firm texture with a slight tart taste until fully ripened, then very sweet. Available mid June - mid July.</p>
      </section>
      <section class="variety">
        <h2 class="variety-name">Riland</h2>
        <p class="variety-description">Very aromatic and sweet, this apricot is orange with a red blush. It has a yellow-orange colored flesh and a round shape. Available mid-June to end of July.</p>
      </section>
    </main>
  </div>
</div>
</body>
</html>
```